Business Card Design Project

I have established a company called "Tidewell" which is a business specialising in psychotherapy/counselling , predominantly for anxiety & depression.

My name is Mel....hence, the Tidewell link. However, Tidewell was also chosen for its reference to green shoots of growth/recovery.

Tidewell is to be "upmarket" and highly professional. I'm keen for the style and colours to reflect this.....taupe/grey with navy/black script, for example.....NO primary colours.

My name needs to be on the card and my mobile number. Not sure, but suspect it should also have my qualifications ( BA (Psych) & BSc (Hons) Psychology). Mobile number 0463 918 207.

```html
<!DOCTYPE html>
<html lang="en">
<head>
<meta charset="utf-8">
<title>Tidewell – Business Card</title>
<link rel="stylesheet" href="https://fonts.googleapis.com/css2?family=Arimo:wght@400&display=swap">
<style>
  :root {
    --paper: #ffffff;
    --ink: #6b7359;
    --stalk: #8e9a79;
    --foliage-light: #dfe4d6;
    --foliage-mid: #c9d1bb;
  }
  html, body {
    margin: 0;
    padding: 0;
    overflow: hidden;
    background: var(--paper);
  }
  .card {
    position: relative;
    width: 1200px;
    height: 840px;
    background: var(--paper);
    overflow: hidden;
    font-family: "Arimo", Arial, sans-serif;
    color: var(--ink);
  }
  .card p { margin: 0; line-height: 1; position: absolute; white-space: nowrap; }

  .foliage {
    position: absolute;
    left: 4px;
    top: 158px;
    width: 302px;
    height: 314px;
    background: linear-gradient(180deg, var(--foliage-mid), var(--foliage-light));
  }
  .stalk {
    position: absolute;
    left: 124px;
    top: 0;
    width: 36px;
    height: 840px;
    background: var(--stalk);
  }

  .brand-name { left: 170px; top: 68px; font-size: 92px; }
  .tagline { left: 416px; top: 184px; font-size: 21px; }
  .person-name { left: 396px; top: 534px; font-size: 83px; }
  .qualifications { left: 541px; top: 580px; font-size: 26px; }
  .mobile-label { left: 336px; top: 639px; font-size: 26px; }
  .mobile-number { left: 424px; top: 620px; font-size: 61px; }
  .services { left: 202px; top: 755px; font-size: 23px; }
</style>
</head>
<body>
  <main class="card">
    <div class="foliage" role="img" aria-label="Illustration area: green leaves sprouting from a plant stalk"></div>
    <div class="stalk" role="img" aria-label="Illustration area: green plant stalk running down the card"></div>

    <p class="brand-name">Tidewell</p>
    <p class="tagline">a place where you can grow...</p>

    <p class="person-name">Mel</p>
    <p class="qualifications">BA (Psych) &amp; BSc (Hons) Psychology</p>
    <p class="mobile-label">mobile</p>
    <p class="mobile-number">0463 918 207</p>

    <p class="services">psychotherapy/counselling specializing in anxiety &amp; depression</p>
  </main>
</body>
</html>
```